Savage Critters Ebook

I have published an ebook - savage critters by Marcus Pellow on Pagewisp - the images I sourced from Chatterfold Marcus Pellow Macro
There are 190 images in the book - I want the pages to be framed in either white or black frame/boarder.
I also need a cover page for the book - I wish to have it in both ebook format and printed also - I prefer landscape as most of the images call for this format.
This is not a book of words - but images of bugs.
I want the presentation of the book more professional -
thanks

```html
<!DOCTYPE html>
<html lang="en">
<head>
<meta charset="utf-8">
<title>Ebook Spread – Page 72</title>
<link rel="stylesheet" href="https://fonts.googleapis.com/css2?family=Roboto+Condensed:wght@400&display=swap">
<style>
  :root {
    --page-bg: #ffffff;
    --spread-black: #000000;
    --gutter-grey: #3a3a3a;
    --accent-yellow: #ffed00;
    --text-white: #ffffff;
    --frame-white: #ffffff;
    --photo-deep: #1d3550;
    --photo-mid: #6f7a63;
    --photo-gold: #c9b21c;
  }
  * { margin: 0; padding: 0; box-sizing: border-box; }
  html, body {
    width: 1200px;
    height: 540px;
    overflow: hidden;
    background: var(--page-bg);
  }
  .canvas {
    position: relative;
    width: 1200px;
    height: 540px;
    background: var(--page-bg);
    font-family: "Roboto Condensed", "Arial Narrow", sans-serif;
  }
  .spread {
    position: absolute;
    left: 59px;
    top: 59px;
    width: 1096px;
    height: 427px;
    background: var(--spread-black);
    overflow: hidden;
  }
  .gutter {
    position: absolute;
    left: 551px;
    top: 0;
    width: 1px;
    height: 100%;
    background: var(--gutter-grey);
  }
  .page-number {
    position: absolute;
    left: -23px;
    top: 183px;
    width: 52px;
    height: 52px;
    border-radius: 50%;
    background: var(--accent-yellow);
    color: var(--spread-black);
    font-size: 15px;
    line-height: 52px;
    text-align: right;
    padding-right: 10px;
  }
  .contact {
    position: absolute;
    right: 607px;
    top: 179px;
    text-align: right;
    font-style: normal;
  }
  .contact-title {
    color: var(--text-white);
    font-size: 19px;
    font-weight: 400;
    font-style: normal;
    line-height: 24px;
    margin-bottom: 6px;
  }
  .contact-line {
    color: var(--accent-yellow);
    font-size: 16px;
    font-style: normal;
    line-height: 26.5px;
  }
  .feature-photo {
    position: absolute;
    left: 632px;
    top: 84px;
    width: 470px;
    height: 252px;
    border: 2px solid var(--frame-white);
    background:
      radial-gradient(ellipse at 20% 45%, #8d9690 0%, transparent 45%),
      radial-gradient(ellipse at 60% 65%, var(--photo-gold) 0%, transparent 55%),
      linear-gradient(100deg, var(--photo-deep) 0%, var(--photo-mid) 40%, var(--photo-gold) 75%, #5f6a3a 100%);
  }
  .caption {
    position: absolute;
    right: 21px;
    top: 368px;
    color: var(--accent-yellow);
    font-size: 23px;
    line-height: 28px;
  }
</style>
</head>
<body>
  <main class="canvas">
    <section class="spread">
      <div class="gutter"></div>

      <div class="page-number">72</div>

      <address class="contact">
        <p class="contact-title">Contact Address Here</p>
        <p class="contact-line">Address Line Here</p>
        <p class="contact-line">Address Line Here</p>
        <p class="contact-line">Address Line Here</p>
      </address>

      <div class="feature-photo" role="img" aria-label="Macro photograph of an insect's head with large compound eyes and yellow bristles"></div>

      <p class="caption">Text Here</p>
    </section>
  </main>
</body>
</html>
```